LKT business card design

Coastal Guard Auxiliary Kin Services exists to provide timely and relevant programs and services to assist commanders with their role to ensure their assigned Families (Soldiers, spouses, children, significant others) have the highest possible level of well-being, and are the "ready" (for deployment, family separation, and self-sufficiency during that separation). We accomplish this task through several functional areas: Leadership (Director), Coordination (Coordinator--coordinates a variety of human services, staff sections, sister agencies, etc. to offer training and support), unit Family Readiness Programs, Junior Learner and Campus Aid, Bereaved Contact Network, Lantern Path Initiative (deployment and reintegration training), Recovery Care (for wounded warriors), Crisis Intervention, and Prevention Education and Training. Our aim is to demonstrate "Kin Above All" in everything we do, because Family Readiness improves Soldier Readiness which improves Army Readiness.

Folks, I've tried to upload the logos I mentioned, with not luck. You can get a look at one version of the Guard Auxiliary Kin Services logo at www.gaks-example.org.

Reason: Extendinig a couple days because I've not yet had any sucess uploading logos I mention in the brief. Hoping to crack the nut on that soon Thanks for your patient work.

Target Market(s)

Army Reserve Commanders, First Sergeants, Adult & Youth Volunteers & Family Members who are called to contribute to Whole Guard Kin readiness by being skilled at handling the challendes of deployment, family separation, and the self-sufficiency required when their Soldier deploys (e.g., fulfilling the Soldiers roles on the homefront while he or she is away)

Industry/Entity Type

Training

Contact Information for Business Card

Dr. Marcus T. Holloway, Director
Family Programs, 4th RDG, CGAWEST
2846 Ridge Lane
Honolulu, HI 96502-4718
808-555-0172 ext. 4820
BB: 808-555-0639
marcus.t.holloway7.staff@postbox-example.net

Requirements
Must have
• Family Programs Logo with text
Nice to have
• 4th RDG and CGAWEST Logo
Should not have
• old GAKS Logo (Green, blue globe with family silhouette)

```html
<!DOCTYPE html>
<html lang="en">
<head>
<meta charset="utf-8">
<title>LKT Business Card</title>
<link rel="stylesheet" href="https://fonts.googleapis.com/css2?family=Source+Sans+3:wght@400;600;700&display=swap">
<style>
  :root {
    --navy: #0f1a45;
    --white: #ffffff;
    --paper: #fbfbfc;
    --edge-grey: #b9bcc4;
    --backdrop: #d6d9de;
    --ink: #1b2142;
    --muted: #8a8d96;
    --orange: #ec5a24;
    --amber: #f3a21b;
    --red: #e4242b;
    --green: #3aa845;
  }
  * { margin: 0; padding: 0; box-sizing: border-box; }
  html, body {
    width: 1200px;
    height: 675px;
    overflow: hidden;
    background: var(--backdrop);
    font-family: "Source Sans 3", "Myriad Pro", sans-serif;
  }
  .business-card {
    position: absolute;
    left: 150px;
    top: 80px;
    width: 900px;
    height: 514px;
    background: var(--paper);
    box-shadow: 0 6px 18px rgba(0,0,0,0.18);
    overflow: hidden;
  }
  .card-art {
    position: absolute;
    inset: 0;
    width: 900px;
    height: 514px;
  }
  .brand-lockup {
    position: absolute;
    left: 330px;
    top: 56px;
    display: flex;
    align-items: center;
    gap: 16px;
  }
  .brand-mark {
    width: 64px;
    height: 64px;
    border-radius: 50%;
    background: var(--navy);
    flex: none;
  }
  .brand-name {
    color: var(--navy);
    font-weight: 700;
    font-size: 26px;
    line-height: 1.05;
    text-transform: uppercase;
    letter-spacing: 0.5px;
  }
  .holder {
    position: absolute;
    left: 180px;
    top: 292px;
    display: flex;
    align-items: center;
    color: var(--white);
    white-space: nowrap;
  }
  .holder-name {
    font-weight: 700;
    font-size: 30px;
    line-height: 1.1;
  }
  .holder-divider {
    display: inline-block;
    width: 2px;
    height: 28px;
    background: var(--white);
    margin: 0 12px;
  }
  .holder-title {
    font-weight: 400;
    font-size: 20px;
    line-height: 1.1;
    padding-top: 4px;
  }
  .contact-block {
    position: absolute;
    left: 300px;
    top: 414px;
    color: var(--ink);
    font-size: 18px;
    line-height: 1.25;
  }
  .contact-phones {
    display: flex;
    gap: 60px;
  }
  .contact-ext {
    position: absolute;
    right: 30px;
    top: 322px;
    color: var(--muted);
    font-size: 19px;
  }
</style>
</head>
<body>
  <div class="business-card">
    <svg class="card-art" viewBox="0 0 900 514" aria-hidden="true">
      <path d="M0,230 C300,230 650,150 900,60" fill="none" stroke="var(--edge-grey)" stroke-width="6"/>
      <path d="M0,240 C300,240 650,160 900,70 L900,300 C700,385 350,405 0,410 Z" fill="var(--navy)"/>
      <path d="M0,410 C350,405 700,385 900,300" fill="none" stroke="var(--edge-grey)" stroke-width="3"/>
      <circle class="partner-badge" cx="112" cy="160" r="58" fill="var(--navy)"/>
      <circle class="partner-badge" cx="836" cy="44" r="32" fill="var(--navy)"/>
      <g class="accent-dashes" stroke-width="5">
        <line x1="40" y1="500" x2="110" y2="500" stroke="var(--orange)"/>
        <line x1="140" y1="500" x2="230" y2="500" stroke="var(--amber)"/>
        <line x1="300" y1="500" x2="390" y2="500" stroke="var(--navy)"/>
        <line x1="420" y1="500" x2="510" y2="500" stroke="var(--red)"/>
        <line x1="540" y1="500" x2="630" y2="500" stroke="var(--green)"/>
        <line x1="660" y1="500" x2="740" y2="500" stroke="var(--red)"/>
        <line x1="770" y1="500" x2="840" y2="500" stroke="var(--orange)"/>
        <line x1="860" y1="500" x2="900" y2="500" stroke="var(--amber)"/>
      </g>
    </svg>

    <div class="brand-lockup">
      <span class="brand-mark"></span>
      <span class="brand-name">Guard Auxiliary<br>Kin Services</span>
    </div>

    <div class="holder">
      <span class="holder-name">Dr. Marcus T. Holloway</span>
      <span class="holder-divider"></span>
      <span class="holder-title">Director Family Programs</span>
    </div>

    <div class="contact-ext">ext. 4820</div>

    <div class="contact-block">
      <div class="contact-phones">
        <span>808-555-0172</span>
        <span>808-555-0639</span>
      </div>
      <div class="contact-email">marcus.t.holloway7.staff@postbox-example.net</div>
      <div class="contact-address">2846 Ridge Lane Honolulu, HI 96502-4718</div>
    </div>
  </div>
</body>
</html>
```